Small IT consulting firm needs a new web site

Quillmark Solutions, LLC is a company based out of Arizona with national presence. We work on both national, multinational, and international projects. We are Brindlesoft Partners. Heavy experience and work with Orbitline Control Kit, Vantra, Deskhub 720 . We offer Architecture, Design, Development, and implementation services. We have a specialty in Deskhub 720 migrations and implementations. We also have a specialized practice in Program and Project Management. The design message should foster a feeling of partnership and experience. Attached is my logo.

```html
<!DOCTYPE html>
<html lang="en">
<head>
<meta charset="utf-8">
<title>Quillmark Solutions, LLC</title>
<link href="https://fonts.googleapis.com/css2?family=Questrial&family=Roboto:ital,wght@0,400;0,500;1,400&display=swap" rel="stylesheet">
<style>
:root{
  --red:#c1122a;
  --red-dark:#9c0d20;
  --ink:#222;
  --text:#444;
  --muted:#777;
  --light:#eeeeee;
  --panel:#6d6d6d;
  --footer:#2a2a2a;
  --white:#fff;
}
*{box-sizing:border-box;margin:0;padding:0}
html,body{width:1200px;height:2586px;overflow:hidden}
body{font-family:"Roboto",Arial,sans-serif;color:var(--text);background:var(--white);position:relative}
.wrap{width:1052px;margin:0 auto;position:relative}
h1,h2,h3,.brand-name{font-family:"Questrial",Arial,sans-serif;font-weight:400}

/* header */
.topline{height:7px;background:#777}
.site-header{height:136px;position:relative}
.brand{position:absolute;left:0;top:22px;display:flex;align-items:center;gap:10px}
.brand-mark{width:40px;height:40px;background:var(--red)}
.brand-name{color:var(--red);font-size:21px;line-height:1.1;width:150px}
.utility{position:absolute;right:0;top:20px;width:514px;height:46px;background:#f1f1f1;border:1px solid #e2e2e2;display:flex;align-items:center;padding:0 14px;font-size:12px;gap:18px}
.utility .call{color:#333;display:flex;align-items:center;gap:8px}
.utility .call b{color:var(--red);font-weight:500}
.utility .chat{color:var(--red);display:flex;align-items:center;gap:6px}
.search{margin-left:auto;width:190px;height:30px;background:#fff;border:1px solid #ddd;display:flex;align-items:center;justify-content:space-between;padding:0 8px;color:#aaa;font-style:italic;font-size:11px}
.main-nav{position:absolute;right:0;top:98px;display:flex;gap:0;font-size:13px;letter-spacing:.3px}
.main-nav a{color:#222;text-decoration:none;padding:0 22px 12px;text-transform:uppercase}
.main-nav a:last-child{padding-right:0}
.main-nav a.active{color:var(--red);border-bottom:3px solid var(--red)}

/* hero */
.hero{height:417px;position:relative;background:linear-gradient(100deg,#2b3133 0%,#3c4648 45%,#5d6b70 60%,#2c3234 100%);overflow:hidden}
.hero-visual{position:absolute;inset:0}
.hero-copy{position:absolute;left:74px;top:58px;width:500px;color:#fff}
.hero-copy h1{font-size:48px;line-height:1.15}
.hero-copy p{font-size:16px;line-height:1.5;margin-top:14px;color:#e6e6e6}
.btn{display:inline-block;background:var(--red);color:#fff;font-size:13px;text-transform:uppercase;text-decoration:none;font-family:"Roboto",sans-serif}
.hero .btn{margin-top:22px;padding:12px 18px}
.dots{position:absolute;left:74px;bottom:38px;display:flex;gap:8px}
.dots i{width:12px;height:12px;border-radius:50%;background:#888}
.dots i:first-child{background:#fff}

/* sections */
.section-title{color:var(--red);font-size:28px;text-align:center}
.welcome{height:255px;text-align:center;padding-top:40px;border-bottom:1px solid #e6e6e6;box-shadow:0 6px 10px -8px rgba(0,0,0,.2)}
.welcome p{font-size:12.5px;line-height:23px;margin:16px auto 0;width:1052px;color:#444}
.welcome .btn{background:#555;margin-top:26px;padding:12px 25px;border:1px solid #333}

.services{height:445px;padding-top:42px}
.service-grid{display:flex;justify-content:space-between;margin-top:30px}
.service-card{width:331px;height:319px;position:relative;overflow:hidden;box-shadow:0 10px 12px -8px rgba(0,0,0,.35);background:var(--red)}
.service-card .top{height:110px;background:linear-gradient(#f6f6f6,#dadada);display:flex;align-items:center;justify-content:center}
.service-card .curve{position:absolute;left:0;top:80px;width:100%;height:60px}
.service-card h3{position:relative;color:#fff;text-align:center;font-family:"Roboto",sans-serif;font-size:18px;line-height:25px;margin-top:42px}
.service-card p{position:relative;color:#f3c9ce;font-size:12.5px;line-height:21px;text-align:center;padding:0 16px;margin-top:12px}

.support{height:305px;background:var(--light);padding-top:32px}
.support-grid{display:flex;justify-content:space-between;margin-top:66px;text-align:center}
.support-item{width:300px}
.support-item h3{font-family:"Roboto",sans-serif;font-size:17px;color:#222}
.support-item p{font-size:12.5px;line-height:21px;margin-top:4px}
.support-item .btn{margin-top:16px;padding:9px 11px;font-size:12px}

.clients{height:187px;padding-top:32px}
.client-row{display:flex;justify-content:space-between;margin-top:20px}
.client{width:164px;height:65px;border:1px solid #cfcfcf;display:flex;align-items:center;justify-content:center;gap:6px;font-size:14px;color:#333;text-align:center;line-height:1.1;font-family:"Roboto",sans-serif;font-weight:500}
.client.solid{background:var(--red-dark);color:#fff}
.client .dot{width:10px;height:10px;border-radius:50%;background:var(--red);flex:none}

.quote{height:273px;background:var(--panel);padding-top:28px}
.quote h2{color:#fff;text-align:center;font-size:27px}
.quote-form{display:flex;justify-content:space-between;margin-top:22px}
.col{width:514px}
.field{height:38px;background:#fff;margin-bottom:12px;font-size:12px;color:#666;padding:11px 12px}
.field.msg{height:88px}
.submit{height:38px;background:linear-gradient(var(--red),var(--red-dark));color:#fff;text-align:center;font-size:13px;line-height:38px;text-transform:uppercase}

.news{height:327px;padding-top:28px}
.news .wrap{display:flex;justify-content:space-between}
.news-col{width:490px}
.news .divider{width:1px;background:#ddd;height:246px;margin-top:8px}
.news h2{color:var(--red);font-size:28px}
.post{margin-top:16px}
.post h3{font-size:19px;color:#222}
.post p{font-size:12.5px;line-height:21px;margin-top:4px}
.more{color:var(--red);font-size:11.5px;font-style:italic;display:block;margin-top:8px}
.member{display:flex;gap:20px;margin-top:20px}
.member .photo{width:88px;height:88px;flex:none;background:linear-gradient(#dfe3e6,#a9b0b5);border:1px solid #ccc}
.member h3{font-size:19px;color:#222}
.member h3 em{color:var(--red);font-size:13px;margin-left:6px}
.member p{font-size:12.5px;line-height:21px;margin-top:4px}

.site-footer{height:234px;background:var(--footer);color:#aaa;padding-top:40px;font-size:12px}
.site-footer .wrap{display:flex}
.f-brand{width:374px}
.f-brand .brand-name{color:#bbb;font-size:18px;display:flex;align-items:center;gap:8px;margin-bottom:40px}
.f-brand .brand-mark{width:30px;height:30px;background:#777}
.f-brand p{line-height:20px}
.f-col h4{color:#fff;font-weight:400;font-size:14px;text-transform:uppercase;margin-bottom:12px;font-family:"Roboto",sans-serif}
.f-company{width:238px}
.f-company .lists{display:flex;gap:48px;line-height:27px}
.f-contact{width:226px;line-height:20px}
.social{display:flex;flex-direction:column;gap:6px}
.social span{display:flex;align-items:center;gap:8px;color:#ddd}
.social i{width:12px;height:12px;border-radius:50%;background:#fff}
</style>
</head>
<body>
<div class="topline"></div>
<header class="site-header">
  <div class="wrap">
    <div class="brand"><span class="brand-mark"></span><span class="brand-name">Quillmark Solutions, LLC</span></div>
    <div class="utility">
      <span class="call">
        <svg width="14" height="14" viewBox="0 0 14 14"><rect x="1" y="1" width="12" height="12" rx="2" fill="#555"/><path d="M4 4c0 4 2 6 6 6l1-2-2-1-1 1c-1-.5-2-1.5-2.5-2.5l1-1-1-2z" fill="#fff"/></svg>
        CALL US: <b>+1-888-555-0142</b></span>
      <span class="chat">
        <svg width="14" height="14" viewBox="0 0 14 14"><circle cx="7" cy="4.5" r="3" fill="#666"/><path d="M1.5 13c0-3 2.5-5 5.5-5s5.5 2 5.5 5z" fill="#666"/></svg>
        LIVE CHAT</span>
      <span class="search">Search
        <svg width="14" height="14" viewBox="0 0 14 14"><circle cx="5.5" cy="5.5" r="4" fill="none" stroke="#c1122a" stroke-width="2"/><path d="M8.5 8.5l4 4" stroke="#c1122a" stroke-width="2.4"/></svg></span>
    </div>
    <nav class="main-nav">
      <a class="active" href="#">Home</a><a href="#">About Us</a><a href="#">Services</a><a href="#">Solutions</a><a href="#">Clients</a><a href="#">Blog</a><a href="#">Careers</a><a href="#">News</a><a href="#">Contact Us</a>
    </nav>
  </div>
</header>

<section class="hero">
  <div class="hero-visual" role="img" aria-label="Businessman touching a glowing digital interface with hexagons and a world map"></div>
  <div class="hero-copy">
    <h1>We Are Committed to Your Success</h1>
    <p>Aliquam molestie, mi et imperdiet euismod, dui purus auctor tellus, et interdum lacus lectus et ante. Sed accumsan sollicitudin sapien..</p>
    <a class="btn" href="#">Read More</a>
  </div>
  <div class="dots"><i></i><i></i><i></i><i></i></div>
</section>

<section class="welcome">
  <h2 class="section-title">Welcome to Our Website</h2>
  <p>Aliquam molestie, mi et imperdiet euismod, dui purus auctor tellus, et interdum lacus lectus et ante. Sed accumsan sollicitudin sapien, sit amet adipiscing turpis gravida ac. In congue, neque ac lobortis volutpat, libero mauris varius mi, vitae suscipit ipsum ligula vitae risus. Duis aliquam nibh a dui iaculis viverra id a velit. Vivamus egestas risus in magna varius commodo. Sed semper viverra egestas. Etiam pretium porttitor lectus, vel ornare neque porta volutpat.</p>
  <a class="btn" href="#">Read More</a>
</section>

<section class="services">
  <div class="wrap">
    <h2 class="section-title">Our Services</h2>
    <div class="service-grid">
      <article class="service-card">
        <div class="top"><svg width="64" height="64" viewBox="0 0 64 64"><circle cx="30" cy="34" r="24" fill="none" stroke="#333" stroke-width="6"/><path d="M18 34l10 10 22-26" fill="none" stroke="#333" stroke-width="7"/><rect x="24" y="2" width="12" height="6" fill="#333"/></svg></div>
        <svg class="curve" viewBox="0 0 331 60" preserveAspectRatio="none"><path d="M0 30 Q165 0 331 22 V60 H0Z" fill="#777"/><path d="M0 42 Q165 14 331 34 V60 H0Z" fill="#c1122a"/></svg>
        <h3>Program &amp;<br>Project Management</h3>
        <p>Aliquam molestie, mi et imperdiet euismod, dui purus auctor tellus, et interdum lacus lectus et ante. Sed accumsan sollicitudin sapien, sit amet adipiscing turpis gravida ac.</p>
      </article>
      <article class="service-card">
        <div class="top"><svg width="64" height="64" viewBox="0 0 64 64"><path d="M8 14l42 42" stroke="#333" stroke-width="9"/><path d="M52 8L10 50l-2 8 8-2 42-42z" fill="none" stroke="#333" stroke-width="4"/></svg></div>
        <svg class="curve" viewBox="0 0 331 60" preserveAspectRatio="none"><path d="M0 30 Q165 0 331 22 V60 H0Z" fill="#777"/><path d="M0 42 Q165 14 331 34 V60 H0Z" fill="#c1122a"/></svg>
        <h3>Technical Architecture,<br>Design &amp; Development</h3>
        <p>Aliquam molestie, mi et imperdiet euismod, dui purus auctor tellus, et interdum lacus lectus et ante. Sed accumsan sollicitudin sapien, sit amet adipiscing turpis gravida ac.</p>
      </article>
      <article class="service-card">
        <div class="top"><svg width="90" height="60" viewBox="0 0 90 60"><rect x="8" y="14" width="22" height="40" rx="6" fill="#333"/><rect x="34" y="8" width="22" height="46" rx="6" fill="#333"/><rect x="60" y="14" width="22" height="40" rx="6" fill="#333"/></svg></div>
        <svg class="curve" viewBox="0 0 331 60" preserveAspectRatio="none"><path d="M0 30 Q165 0 331 22 V60 H0Z" fill="#777"/><path d="M0 42 Q165 14 331 34 V60 H0Z" fill="#c1122a"/></svg>
        <h3>Staff Augmentation &amp;<br>Implementation</h3>
        <p>Aliquam molestie, mi et imperdiet euismod, dui purus auctor tellus, et interdum lacus lectus et ante. Sed accumsan sollicitudin sapien, sit amet adipiscing turpis gravida ac.</p>
      </article>
    </div>
  </div>
</section>

<section class="support">
  <div class="wrap">
    <h2 class="section-title">Our Support</h2>
    <div class="support-grid">
      <div class="support-item"><h3>Orbitline Control Kit</h3><p>Aliquam molestie, mi et imperdiet euismod, dui purus auctor tellus, et interdum lacus lectus et ante.</p><a class="btn" href="#">Read More</a></div>
      <div class="support-item"><h3>Vantra</h3><p>Aliquam molestie, mi et imperdiet euismod, dui purus auctor tellus, et interdum lacus lectus et ante.</p><a class="btn" href="#">Read More</a></div>
      <div class="support-item"><h3>Deskhub 720</h3><p>Aliquam molestie, mi et imperdiet euismod, dui purus auctor tellus, et interdum lacus lectus et ante.</p><a class="btn" href="#">Read More</a></div>
    </div>
  </div>
</section>

<section class="clients">
  <div class="wrap">
    <h2 class="section-title">Our Clients</h2>
    <div class="client-row">
      <div class="client solid">Harrowgate Bank</div>
      <div class="client"><span class="dot"></span>Lumen Crest Group</div>
      <div class="client">Keystone Ledger</div>
      <div class="client">Halvorsen Controls</div>
      <div class="client">Ironvale Automation</div>
      <div class="client">Mereford Health</div>
    </div>
  </div>
</section>

<section class="quote">
  <div class="wrap">
    <h2>Request a Quote</h2>
    <div class="quote-form">
      <div class="col"><div class="field">Name</div><div class="field">Email Address</div><div class="field">Phone No.</div></div>
      <div class="col"><div class="field msg">Message</div><div class="submit">Submit Now</div></div>
    </div>
  </div>
</section>

<section class="news">
  <div class="wrap">
    <div class="news-col">
      <h2>Blog Posts</h2>
      <article class="post"><h3>Lorem ipsum dolor sit ame...</h3><p>Aliquam molestie, mi et imperdiet euismod, dui purus auctor tellus, et interdum lacus lectus et ante. Sed accumsan sollicitudin sapien, sit amet adipiscing turpis gravida ac...</p><span class="more">Continue Reading</span></article>
      <article class="post"><h3>Lorem ipsum dolor sit ame...</h3><p>Aliquam molestie, mi et imperdiet euismod, dui purus auctor tellus, et interdum lacus lectus et ante. Sed accumsan sollicitudin sapien, sit amet adipiscing turpis gravida ac...</p><span class="more">Continue Reading</span></article>
    </div>
    <div class="divider"></div>
    <div class="news-col">
      <h2>Our Team</h2>
      <div class="member"><div class="photo" role="img" aria-label="Portrait of a team director"></div><div><h3>Name Heading <em>(Director)</em></h3><p>Aliquam molestie, mi et imperdiet euismod, dui purus auctor tellus, et interdum lacus lectus et ante. Sed accumsan sollicitudin...</p><span class="more">Read More</span></div></div>
      <div class="member"><div class="photo" role="img" aria-label="Portrait of a team director"></div><div><h3>Name Heading <em>(Director)</em></h3><p>Aliquam molestie, mi et imperdiet euismod, dui purus auctor tellus, et interdum lacus lectus et ante. Sed accumsan sollicitudin...</p><span class="more">Read More</span></div></div>
    </div>
  </div>
</section>

<footer class="site-footer">
  <div class="wrap">
    <div class="f-brand">
      <div class="brand-name"><span class="brand-mark"></span>Quillmark Solutions, LLC</div>
      <p>Copyright ©2015.CompanyName,All Right Reserved<br>Privacy Policy &nbsp;|&nbsp; Term Of Services</p>
    </div>
    <div class="f-col f-company">
      <h4>Company</h4>
      <div class="lists"><div>Home<br>About Us<br>Services<br>Solutions<br>Clients</div><div>Blog<br>Careers<br>News<br>Contact Us</div></div>
    </div>
    <div class="f-col f-contact">
      <h4>Contact Us</h4>
      418 E Mesa Vista Drive<br>Suite 205-310<br>Phoenix, AZ 85016-2211<br>Local: +1-602-555-0187<br>Toll Free: +1-888-555-0142<br>Fax: +1-480-555-0163<br>hello@quillmarksolutions.co
    </div>
    <div class="f-col">
      <h4>Connect Us</h4>
      <div class="social"><span><i></i>Chirpline</span><span><i></i>Facepage</span><span><i></i>Linkwork</span><span><i></i>Globeplus</span><span><i></i>Viewtube</span></div>
    </div>
  </div>
</footer>
</body>
</html>
```